I own a rendering company which is in the construction industry i already have a logo i would like i

I want to make the website look professional and blends nicely with the logo, if i can have contact information and photos logos and a place where they can email me for job quotes or request and we want to win the big jobs so think also corporate in conjunction with construction. also an area for brief description and about us

Target Market(s)

Home owners/Investors, Small and major construction companies

Industry/Entity Type

Construction Company

Coding

Coded - Design and coding required

Number of Pages Required

3 page

Font styles to use
Serif
Sans Serif

Colors

Designer to choose colors to be used in the design.

Requirements
Must have
• An area for pictures to show with fade changes or clicking options(of white set walls, acrylic render expensive houses walls) an "about us" section. An area to where potential customers can email us (a writing box) where we can receive request for quotes and potential jobs. all contact information and license numbers
Nice to have
• pictures of plastered walls (posh elegant) and rendered walls acrylic and cement render
Should not have
• anything boring plain font etc

```html
<!DOCTYPE html>
<html lang="en">
<head>
<meta charset="utf-8">
<title>Ashbury Walls – Professional Construction Company</title>
<link rel="stylesheet" href="https://fonts.googleapis.com/css2?family=Montserrat:wght@400;500;600;700&family=Lato:wght@400;700&display=swap">
<style>
:root{
  --red:#e31b23;
  --dark:#262626;
  --darker:#1f1f1f;
  --ink:#222222;
  --muted:#777777;
  --pink:#fbe3e5;
  --grey:#eeeeee;
  --white:#ffffff;
  --line:#e2e2e2;
}
*{box-sizing:border-box;margin:0;padding:0}
html,body{width:1200px;height:3416px;overflow:hidden;background:var(--white)}
body{position:relative;font-family:"Lato",sans-serif;color:var(--ink)}
.abs{position:absolute}
h1,h2,h3,h4,.nav,.btn{font-family:"Montserrat",sans-serif}
p{font-size:11px;line-height:18px;color:var(--muted)}
.btn{display:inline-block;font-size:11px;font-weight:600;text-transform:uppercase;padding:0 22px;line-height:32px;height:32px}
.btn-red{background:var(--red);color:var(--white)}
.btn-white{background:var(--white);color:var(--ink)}

/* wordmark */
.wordmark{display:flex;align-items:center;gap:9px;font-family:"Montserrat",sans-serif;font-weight:600;color:var(--red);font-size:19px;white-space:nowrap}
.wordmark i{width:16px;height:16px;border-radius:50%;background:var(--red);display:inline-block}
.brand{left:176px;top:30px}

/* header contacts */
.contact{top:18px;display:flex;align-items:center;gap:12px}
.contact .ico{width:32px;height:32px;border:1.5px solid var(--red);border-radius:50%;display:flex;align-items:center;justify-content:center}
.contact strong{display:block;font-size:11px;color:var(--ink);font-family:"Montserrat",sans-serif;font-weight:500}
.contact span{display:block;font-size:9.5px;color:var(--muted)}

/* hero */
.hero{left:6px;top:102px;width:1184px;height:451px;background:linear-gradient(120deg,#3b2a1c 0%,#7a5a3a 35%,#b98a48 55%,#4a3a2c 80%,#1e1a16 100%)}
.nav{left:173px;top:80px;width:856px;height:50px;background:var(--dark);display:flex;align-items:center;z-index:2}
.nav a{color:var(--white);font-size:10.5px;font-weight:500;text-transform:uppercase;padding:0 17px;text-decoration:none}
.nav a.active{color:var(--red)}
.nav .quote{margin-left:auto;background:var(--red);height:50px;line-height:50px;padding:0 22px;font-weight:600}
.hero-box{left:160px;top:250px;width:440px;height:92px;background:rgba(70,70,70,.78);padding:8px 16px}
.hero-box h1{font-size:17px;font-weight:700;color:var(--white);text-transform:uppercase}
.hero-box p{color:var(--white);font-size:16px;line-height:23px;margin-top:4px}
.hero-btns{left:173px;top:360px;display:flex;gap:10px}

/* services */
.svc-photos{left:173px;top:524px;width:854px;height:189px;display:flex;gap:4px}
.svc-photos div{flex:1}
.svc{top:677px;width:280px;text-align:center}
.svc .circle{width:62px;height:62px;border-radius:50%;background:var(--red);margin:0 auto;display:flex;align-items:center;justify-content:center}
.svc h3{font-size:12.5px;font-weight:500;text-transform:uppercase;margin-top:18px;letter-spacing:.3px}
.svc .rule{width:30px;height:2px;background:#f0b400;margin:8px auto 14px}
.svc p{font-size:10px;line-height:17px;padding:0 28px}

/* cta */
.cta{left:0;top:893px;width:1200px;height:154px;background:var(--pink)}
.cta h2{left:220px;top:45px;font-size:21px;font-weight:500;color:#2a3a55;line-height:28px;text-transform:uppercase;font-family:"Lato",sans-serif}
.cta .btn{left:720px;top:50px;height:44px;line-height:44px;font-size:13px;border-radius:3px}

/* featured */
.featured{left:0;top:1113px;width:1200px;height:321px;background:var(--dark)}
.featured h4{left:162px;top:48px;color:var(--white);font-size:12px;font-weight:500;text-transform:uppercase}
.arrows{left:957px;top:40px;display:flex;gap:5px}
.arrows span{width:25px;height:25px;background:#4a4a4a;display:flex;align-items:center;justify-content:center}
.reel{left:8px;top:96px;display:flex;gap:27px}
.reel div{width:214px;height:159px}

/* steps */
.step{top:1488px;width:270px}
.step .num{font-family:"Montserrat",sans-serif;color:var(--red);font-size:22px;font-weight:500}
.step h3{font-size:12.5px;font-weight:500;margin:10px 0 12px}
.step p{font-size:10px;line-height:17px}
.divider{left:173px;top:1676px;width:854px;height:1px;background:var(--line)}

/* experience */
.exp{left:173px;top:1736px;width:420px}
.exp h3{font-size:13px;font-weight:500;text-transform:uppercase;margin-bottom:12px}
.exp p{font-size:10px;line-height:17px}
.exp-cols{display:flex;gap:40px;margin-top:26px}
.exp-cols h4{font-size:12px;font-weight:500;margin-bottom:6px}
.exp .btn{margin-top:22px;height:30px;line-height:30px;font-size:10px}
.house{left:660px;top:1712px;width:290px;height:270px;background:linear-gradient(160deg,#e2c28e 0%,#c69b5e 55%,#8a6a40 100%)}

/* banner */
.banner{left:6px;top:2022px;width:1188px;height:373px;background:linear-gradient(100deg,#2a1c12 0%,#6a4a2e 30%,#3a2a1e 55%,#8a6a4a 80%,#c8b294 100%)}
.banner-text{left:0;top:2140px;width:1200px;text-align:center;color:var(--white)}
.banner-text h2{font-size:42px;font-weight:500;line-height:48px;text-transform:uppercase}
.banner-text h2 em{font-style:normal;color:var(--red)}
.banner-text h2.big{font-weight:700}
.banner-text p{color:var(--white);font-size:14px;margin-top:4px}

/* posts */
.post{top:2455px;width:272px}
.post .img{height:198px}
.post h3{font-size:12px;font-weight:500;text-transform:uppercase;margin:30px 0 10px;padding:0 22px;line-height:17px}
.post p{padding:0 22px;font-size:10px;line-height:17px}
.post .more{display:block;padding:0 22px;margin-top:12px;font-family:"Montserrat",sans-serif;font-size:10px;color:var(--red);text-transform:uppercase;font-weight:500}

/* clients */
.clients{left:0;top:2835px;width:1200px;height:257px;background:var(--grey)}
.clients h2{left:0;top:50px;width:1200px;text-align:center;font-size:16px;font-weight:500;text-transform:uppercase}
.logos{left:173px;top:107px;display:flex;gap:11px}
.logos div{width:162px;height:82px;background:var(--white);display:flex;align-items:center;justify-content:center;gap:8px;font-family:"Lato",sans-serif;font-weight:700;color:#666;font-size:15px}
.logos i{width:12px;height:12px;border-radius:50%;background:#999;display:inline-block}
.dots{left:590px;top:217px;display:flex;gap:8px}
.dots span{width:6px;height:6px;border-radius:50%;background:#999}
.dots span.on{background:var(--red)}

/* footer */
.footer{left:0;top:3092px;width:1200px;height:324px;background:var(--darker)}
.foot-brand{left:210px;top:50px}
.footer p{color:#8a8a8a;font-size:10px;line-height:16px}
.foot-about{left:173px;top:100px;width:240px}
.footer h4{color:var(--white);font-size:11px;font-weight:500;text-transform:uppercase}
.foot-rule{width:30px;height:2px;background:var(--red);margin-top:8px}
.tags{left:467px;top:52px;width:240px}
.tags ul{list-style:none;display:flex;flex-wrap:wrap;gap:8px;margin-top:40px}
.tags li{font-family:"Montserrat",sans-serif;font-size:9px;color:#999;border:1px solid #444;padding:5px 10px;text-transform:uppercase}
.hours{left:758px;top:52px;width:270px}
.hours table{width:100%;border-collapse:collapse;margin-top:30px}
.hours td{font-size:10px;color:#999;padding:0;height:29px;border-bottom:1px solid #3a3a3a}
.hours td:last-child{text-align:right;color:var(--white)}
</style>
</head>
<body>

<!-- header -->
<div class="abs brand wordmark"><i></i>Ashbury Walls</div>
<div class="abs contact" style="left:553px">
  <div class="ico"><svg width="14" height="14" viewBox="0 0 14 14"><path d="M1 7 L7 1.5 L13 7 M3 6 V12.5 H11 V6" fill="none" stroke="#e31b23" stroke-width="1.6"/></svg></div>
  <div><strong>112 Your Adress 23</strong><span>Washington DC 1234</span></div>
</div>
<div class="abs contact" style="left:729px">
  <div class="ico"><svg width="14" height="14" viewBox="0 0 14 14"><path d="M3 1.5 L5.5 4 L4 6 Q6 9 8 10 L10 8.5 L12.5 11 L10.5 13 Q4 12 1 4 Z" fill="#e31b23"/></svg></div>
  <div><strong>Call us anytime</strong><span>+1 555 1234</span></div>
</div>
<div class="abs contact" style="left:888px">
  <div class="ico"><svg width="14" height="14" viewBox="0 0 14 14"><rect x="1.5" y="3" width="11" height="8" fill="none" stroke="#e31b23" stroke-width="1.4"/><path d="M1.5 3 L7 8 L12.5 3" fill="none" stroke="#e31b23" stroke-width="1.4"/></svg></div>
  <div><strong>Send us a mail</strong><span>mail@domain.com</span></div>
</div>

<!-- hero -->
<div class="abs hero" role="img" aria-label="Close-up photo of a worker in gloves and a hard hat drilling into a wooden board"></div>
<nav class="abs nav">
  <a class="active">Home</a><a>Projects</a><a>What we do</a><a>About us</a><a>Blog</a><a>Shop</a><a>Contact us</a>
  <a><svg width="11" height="11" viewBox="0 0 12 12"><circle cx="5" cy="5" r="3.6" fill="none" stroke="#fff" stroke-width="1.6"/><path d="M7.6 7.6 L11 11" stroke="#fff" stroke-width="1.6"/></svg></a>
  <a class="quote">Get a quote</a>
</nav>
<div class="abs hero-box">
  <h1>Professional Construction Company</h1>
  <p>Lorem ipsum dolor sit amet, consectetur adipiscing elit. Quisque nec erat erat. Integer blandit, nulla quis.</p>
</div>
<div class="abs hero-btns"><span class="btn btn-red">Explore</span><span class="btn btn-white">Buy now</span></div>

<!-- services -->
<div class="abs svc-photos">
  <div role="img" aria-label="Photo of a carpenter measuring timber in a workshop" style="background:linear-gradient(135deg,#c9b8a0,#8a5a44 60%,#5a3e30)"></div>
  <div role="img" aria-label="Photo of hands drafting an architectural plan with drawing tools" style="background:linear-gradient(135deg,#eeeae4,#d0ccc4 60%,#b9a98e)"></div>
  <div role="img" aria-label="Photo of a circular saw cutting a plank with sparks" style="background:linear-gradient(135deg,#7a6a58,#c49a5e 50%,#3a3430)"></div>
</div>
<div class="abs svc" style="left:173px">
  <div class="circle"><svg width="22" height="22" viewBox="0 0 22 22"><circle cx="11" cy="11" r="6" fill="none" stroke="#fff" stroke-width="2.4"/><circle cx="11" cy="11" r="2" fill="#fff"/><path d="M11 1v4M11 17v4M1 11h4M17 11h4M4 4l3 3M15 15l3 3M18 4l-3 3M7 15l-3 3" stroke="#fff" stroke-width="2"/></svg></div>
  <h3>Constructions</h3><div class="rule"></div>
  <p>Lorem ipsum dolor sit amet consectetur elit adipiscing praesent pellentesque varius ligula sit eleifend diam cursus nec.</p>
</div>
<div class="abs svc" style="left:460px">
  <div class="circle"><svg width="22" height="22" viewBox="0 0 22 22"><path d="M2 11 L11 3 L20 11 H17 V19 H13 V14 H9 V19 H5 V11 Z" fill="#fff"/></svg></div>
  <h3>Interior Design</h3><div class="rule"></div>
  <p>Lorem ipsum dolor sit amet consectetur elit adipiscing praesent pellentesque varius ligula sit eleifend diam cursus nec.</p>
</div>
<div class="abs svc" style="left:747px">
  <div class="circle"><svg width="22" height="22" viewBox="0 0 22 22"><path d="M4 18 L13 9" stroke="#fff" stroke-width="3" stroke-linecap="round"/><path d="M12 4 A5 5 0 1 0 18 10 L15 10 L12 7 Z" fill="#fff"/></svg></div>
  <h3>Renovation</h3><div class="rule"></div>
  <p>Lorem ipsum dolor sit amet consectetur elit adipiscing praesent pellentesque varius ligula sit eleifend diam cursus nec.</p>
</div>

<!-- cta -->
<section class="abs cta">
  <h2 class="abs">Fast and reliable service for your<br>project or a quick fix, we do it all!</h2>
  <span class="abs btn btn-red">Request your quote</span>
</section>

<!-- featured work -->
<section class="abs featured">
  <h4 class="abs">Featured work</h4>
  <div class="abs arrows">
    <span><svg width="8" height="10" viewBox="0 0 8 10"><path d="M6 1 L2 5 L6 9" fill="none" stroke="#aaa" stroke-width="1.5"/></svg></span>
    <span><svg width="8" height="10" viewBox="0 0 8 10"><path d="M2 1 L6 5 L2 9" fill="none" stroke="#aaa" stroke-width="1.5"/></svg></span>
  </div>
  <div class="abs reel">
    <div role="img" aria-label="Photo of a bright white kitchen with wooden counter" style="background:linear-gradient(160deg,#f2f0ec,#d9cfc0 60%,#a88a5c)"></div>
    <div role="img" aria-label="Photo of a modern kitchen with dark cabinets" style="background:linear-gradient(160deg,#e8e6e2,#8a8680 55%,#3a3836)"></div>
    <div role="img" aria-label="Photo of an open-plan living and dining room" style="background:linear-gradient(160deg,#d8cfc2,#8a6a4a 55%,#4a3a2e)"></div>
    <div role="img" aria-label="Photo of a light dining room with timber floor" style="background:linear-gradient(160deg,#f4f2ee,#ddd6ca 55%,#b08a62)"></div>
    <div role="img" aria-label="Photo of a living room with timber wall and staircase" style="background:linear-gradient(160deg,#efe9e0,#b7926a 55%,#5e4634)"></div>
  </div>
</section>

<!-- steps -->
<div class="abs step" style="left:173px">
  <div class="num">01.</div><h3>Project Planning</h3>
  <p>Lorem ipsum dolor sit amet, consectetur adipiscing elit eiusmod tempor incididunt ut labore dolore magna aliqua. Ut enim minim veniam, quis nostrud exercitation ullamco laboris nisi ut aliquip commodo consequat.</p>
</div>
<div class="abs step" style="left:465px">
  <div class="num">02.</div><h3>Project Crafting</h3>
  <p>Lorem ipsum dolor sit amet, consectetur adipiscing elit eiusmod tempor incididunt ut labore dolore magna aliqua. Ut enim minim veniam, quis nostrud exercitation ullamco laboris nisi ut aliquip commodo consequat.</p>
</div>
<div class="abs step" style="left:756px">
  <div class="num">03.</div><h3>Product Delivery</h3>
  <p>Lorem ipsum dolor sit amet, consectetur adipiscing elit eiusmod tempor incididunt ut labore dolore magna aliqua. Ut enim minim veniam, quis nostrud exercitation ullamco laboris nisi ut aliquip commodo consequat.</p>
</div>
<div class="abs divider"></div>

<!-- experience -->
<div class="abs exp">
  <h3>Over 25 years of experience</h3>
  <p>I am text block. Click edit button to change this text. Lorem ipsum dolor sit amet, consectetur adipiscing elit. Ut elit tellus, luctus nec ullamcorper mattis, pulvinar dapibus leo. Lorem ipsum dolor sit amet, consectetur adipiscing elit.</p>
  <div class="exp-cols">
    <div><h4>Free Consultation</h4><p>Quisque semper iaculis velit, nec tristique quam bibendum et in molestie nulla.</p></div>
    <div><h4>Free Customer Support</h4><p>Quisque semper iaculis velit, nec tristique quam bibendum et in molestie nulla.</p></div>
  </div>
  <span class="btn btn-red">Read more</span>
</div>
<div class="abs house" role="img" aria-label="Illustration of a cardboard house on large off-road wheels"></div>

<!-- banner -->
<div class="abs banner" role="img" aria-label="Photo of a bearded craftsman in a plaid shirt working at a bench"></div>
<div class="abs banner-text">
  <h2>Make it happen</h2>
  <h2 class="big">Your dream <em>home</em></h2>
  <p>Trusted by over 300+ of the world's leading brands</p>
</div>

<!-- posts -->
<div class="abs post" style="left:173px">
  <div class="img" role="img" aria-label="Photo of a small house model with a yellow hard hat and blueprints" style="background:linear-gradient(140deg,#e9e4da,#c9a96a 50%,#f2c12e 80%)"></div>
  <h3>From idea to realisation</h3>
  <p>Lorem ipsum dolor sit amet, consectetur adipiscing elit. Maecenas scelerisque lacinia vestibulum.</p>
  <span class="more">Read more</span>
</div>
<div class="abs post" style="left:465px">
  <div class="img" role="img" aria-label="Photo of a trowel spreading cement on a brick wall" style="background:linear-gradient(140deg,#d6d2cc,#9a948c 55%,#6a645e)"></div>
  <h3>Home renovations with no fuss</h3>
  <p>Lorem ipsum dolor sit amet, consectetur adipiscing elit. Maecenas scelerisque lacinia vestibulum.</p>
  <span class="more">Read more</span>
</div>
<div class="abs post" style="left:757px">
  <div class="img" role="img" aria-label="Photo of a mitre saw cutting timber" style="background:linear-gradient(140deg,#eeeeee,#b8b4ae 50%,#e2b530 85%)"></div>
  <h3>Make your home your paradise</h3>
  <p>Lorem ipsum dolor sit amet, consectetur adipiscing elit. Maecenas scelerisque lacinia vestibulum.</p>
  <span class="more">Read more</span>
</div>

<!-- clients -->
<section class="abs clients">
  <h2 class="abs">Our clients</h2>
  <div class="abs logos">
    <div><i></i>Northgate</div>
    <div>Harbor &amp; Co</div>
    <div>Stoneway</div>
    <div><i></i>Brickfield</div>
    <div>Ironbridge</div>
  </div>
  <div class="abs dots"><span class="on"></span><span></span></div>
</section>

<!-- footer -->
<footer class="abs footer">
  <div class="abs foot-brand wordmark"><i></i>Ashbury Walls</div>
  <div class="abs foot-about">
    <p>Lorem ipsum dolor sit amet, consectetur adipiscing elit. Nam turpis quam, sodales in ante sagittis efficitur mauris congue velit interdum in nulla.</p>
    <p style="margin-top:8px">Nam turpis quam, sodales in ante sagittis, varius efficitur mauris. Lorem ipsum dolor sit amet consectetur.</p>
  </div>
  <div class="abs tags">
    <h4>Tags</h4><div class="foot-rule"></div>
    <ul><li>Big</li><li>Buildings</li><li>Custom work</li><li>Handyman</li><li>Home</li><li>Modern</li><li>Simple</li><li>Wood worker</li></ul>
  </div>
  <div class="abs hours">
    <h4>Working hours</h4><div class="foot-rule"></div>
    <table>
      <tr><td>Monday</td><td>8 am - 17 pm</td></tr>
      <tr><td>Tuesday</td><td>8 am - 17 pm</td></tr>
      <tr><td>Wednesday</td><td>8 am - 17 pm</td></tr>
      <tr><td>Thursday</td><td>8 am - 17 pm</td></tr>
      <tr><td>Friday</td><td>8 am - 17 pm</td></tr>
      <tr><td>Saturday</td><td>8 am - 17 pm</td></tr>
    </table>
  </div>
</footer>

</body>
</html>
```